Business Cards and Logo

KWM - Personal Injury Attorneys is the name of the firm.
We are personal injury lawyers. We want a crisp, modern and impactful design.
Color schemes are white, matte black and light grey OR white, matte black and red OR white, matte black and a nice blue or yellow.
For logo - we don’t want typical logos like scales of justice or a hammer. We want a general design with the KWM letters.
Target Market(s)
People who need attorneys.
Industry/Entity Type
Law Firm
Contact Information for Business Card
Back side: text: Westmere - Calder Bay - Sunhollow - Pine Harbor
Front side
Name of firm and logo.
Marco Feltrovski
812 W. Colter Ave. 4th Floor
Ashford Hills, CA 90412
(818)555-0172 (c)
(818)555-0194 (o)
Marco@fieldcounselwest.example
Logo Text
KWM
Font styles to use
Other font styles liked:
- Musk - regular. Military - regular. Moonglade. Future. Or similar fonts.
Requirements
Must have
- See above. Nothing else to provide.
- KWM - Personal Injury Attorneys is the name of the firm.
- We are personal injury lawyers. We want a crisp, modern and impactful design.
- Color schemes are white, matte black and light grey OR white, matte black and red OR white, matte black and a nice blue or yellow.
- For logo - we don’t want typical logos like scales of justice or a hammer. We want a general design with the KWM letters.
Nice to have
- See above - nothing else to provide.
Should not have

```html
<!DOCTYPE html>
<html lang="en">
<head>
<meta charset="utf-8">
<title>KWM Personal Injury Attorneys – Business Cards</title>
<link rel="stylesheet" href="https://fonts.googleapis.com/css2?family=Montserrat:wght@300;400&family=Cinzel:wght@400&family=Open+Sans:ital,wght@0,400;1,400&display=swap">
<style>
  :root{
    --bg:#e6e3de;
    --ink:#1a1a1a;
    --matte:#111111;
    --grey:#6d6d6d;
    --paper:#ffffff;
    --rule:#2a2a2a;
    --body-text:#333333;
  }
  *{box-sizing:border-box;margin:0;padding:0}
  html,body{width:1200px;height:900px;overflow:hidden}
  body{background:var(--bg);position:relative;font-family:"Montserrat",sans-serif;color:var(--ink)}

  .brand-lockup{position:absolute;left:0;top:90px;width:1200px;text-align:center;
    font-family:"Montserrat",sans-serif;font-weight:300;color:var(--ink)}
  .brand-lockup .initials{font-size:84px;letter-spacing:6px;line-height:1}
  .brand-lockup .firm{font-size:34px;margin-top:26px;line-height:1}
  .brand-lockup .practice{font-size:17px;letter-spacing:14px;margin-top:14px;padding-left:14px}

  .card{position:absolute;top:440px;width:550px;height:314px;overflow:hidden;
    box-shadow:0 10px 26px rgba(0,0,0,.25)}
  .card-front{left:30px;background:var(--paper)}
  .card-back{left:620px;background:var(--matte)}

  .card-front .base-band{position:absolute;left:0;right:0;bottom:0;height:30px;background:var(--matte)}

  .front-lockup{position:absolute;right:40px;top:28px;text-align:center;font-family:"Montserrat",sans-serif;
    font-weight:400;color:var(--grey)}
  .front-lockup .initials{font-size:34px;letter-spacing:3px;line-height:1}
  .front-lockup .firm{font-size:15px;margin-top:8px;line-height:1}
  .front-lockup .practice{font-size:8px;letter-spacing:6px;margin-top:4px;padding-left:6px}

  .card-front .holder-name{position:absolute;left:38px;top:100px;font-family:"Cinzel",serif;
    font-size:25px;letter-spacing:1px;color:var(--ink);line-height:1}
  .card-front .name-rule{position:absolute;left:38px;right:40px;top:140px;height:1px;background:var(--rule)}

  .contact-list{position:absolute;left:38px;top:158px;list-style:none;font-family:"Open Sans",sans-serif;
    font-style:italic;font-size:12.5px;color:var(--body-text)}
  .contact-list li{display:flex;align-items:center;height:22px}
  .contact-list svg{width:12px;height:12px;margin-right:8px;fill:var(--ink)}

  .office-address{position:absolute;right:40px;top:222px;text-align:right;font-family:"Open Sans",sans-serif;
    font-style:normal;font-size:13.5px;line-height:24px;color:var(--body-text)}

  .back-lockup{position:absolute;left:0;right:0;top:78px;text-align:center;color:var(--grey);
    font-family:"Montserrat",sans-serif;font-weight:400}
  .back-lockup .initials{font-size:52px;letter-spacing:4px;line-height:1}
  .back-lockup .firm{font-size:23px;margin-top:14px;line-height:1}
  .back-lockup .practice{font-size:11px;letter-spacing:10px;margin-top:8px;padding-left:10px}
  .office-cities{position:absolute;left:0;right:0;top:238px;text-align:center;color:var(--grey);
    font-family:"Montserrat",sans-serif;font-size:10.5px;letter-spacing:1px}
  .office-cities .sep{margin:0 12px}
</style>
</head>
<body>

  <header class="brand-lockup">
    <div class="initials">KWM</div>
    <div class="firm">PERSONAL INJURY</div>
    <div class="practice">ATTORNEYS</div>
  </header>

  <section class="card card-front">
    <div class="front-lockup">
      <div class="initials">KWM</div>
      <div class="firm">PERSONAL INJURY</div>
      <div class="practice">ATTORNEYS</div>
    </div>

    <div class="holder-name">MARCO FELTROVSKI</div>
    <div class="name-rule"></div>

    <ul class="contact-list">
      <li>
        <svg viewBox="0 0 12 12" aria-hidden="true"><path d="M3 0h6a1 1 0 0 1 1 1v10a1 1 0 0 1-1 1H3a1 1 0 0 1-1-1V1a1 1 0 0 1 1-1zm0 1.5v8h6v-8zM5.5 10h1v1h-1z"/></svg>
        (818)555-0172
      </li>
      <li>
        <svg viewBox="0 0 12 12" aria-hidden="true"><path d="M3 .5l2 2.2-1.1 1.4c.6 1.5 1.9 2.9 3.5 3.6L8.7 6.6 11 8.6 9.8 10.9C5.3 10.6 1.2 6.6 1 2.1z"/></svg>
        (818)555-0194
      </li>
      <li>
        <svg viewBox="0 0 12 12" aria-hidden="true"><path d="M0 2h12v8H0zm1.2 1L6 6.4 10.8 3zM1 4.2V9h10V4.2L6 7.7z"/></svg>
        Marco@fieldcounselwest.example
      </li>
    </ul>

    <address class="office-address">
      812 W. Colter Ave. 4th Floor<br>
      Ashford Hills, CA 90412
    </address>

    <div class="base-band"></div>
  </section>

  <section class="card card-back">
    <div class="back-lockup">
      <div class="initials">KWM</div>
      <div class="firm">PERSONAL INJURY</div>
      <div class="practice">ATTORNEYS</div>
    </div>
    <div class="office-cities">
      WESTMERE<span class="sep">|</span>CALDER BAY<span class="sep">|</span>SUNHOLLOW<span class="sep">|</span>PINE HARBOR
    </div>
  </section>

</body>
</html>
```